Glimmerseal pond linings website template

We need a template for our new website. Glimmerseal is currently marketed through www.tarpavale.com.au, and we are moving the pond/dam linings to a dedicated site www.glimmerseal.com.au

The site is essentially brochureware. The content (less landing page & photo gallery) is on the new site to give you a better idea of what we do. We are also on Facebook.com/glimmerseal

We are looking for a template/style which we can adapt to the different sections of the site as required. We also get a lot of phone/tablet visitors so an alternative mobile layout would be a bonus, but by no means required.

I am proficient in HTML/CSS & javascript so can code most designs thrown at me.

Any icons or interface fonts should be freely available web fonts where possible.

Target Market(s)

We are targeting both landscape professionals (design & construction) as well as the DIY market for ponds/wateragrdens.

Industry/Entity Type

Moving

Requirements
Must have
• We need a design (preferably layered PSD or AI) as basis for our overall site look and feel. Fonts/iconography/layout are where we are lacking. We can do the HTML/CSS/JS/PHP internally.
Nice to have
• A style guide either in file or separate would be nice.
Layers with effect (i.e.. :hover, CSS3 transition endpoints, etc)

```html
<!DOCTYPE html>
<html lang="en">
<head>
<meta charset="utf-8">
<title>Glimmerseal – Pond Liners</title>
<link href="https://fonts.googleapis.com/css2?family=Open+Sans:wght@400;600;700&display=swap" rel="stylesheet">
<style>
:root{
  --lime:#c5d831;
  --lime-dark:#a9bd1e;
  --navy:#0b3a78;
  --navy-deep:#0a2f66;
  --orange:#f47a10;
  --text:#1a1a1a;
  --muted:#555;
  --page:#ffffff;
  --band:#ededed;
  --fb:#2f6b2a;
  --tw:#c5d831;
  --li:#4f8a2a;
}
*{box-sizing:border-box;margin:0;padding:0}
html,body{width:720px;height:1200px;overflow:hidden}
body{font-family:"Open Sans",Arial,sans-serif;background:var(--page);color:var(--text);position:relative}
.top-band{position:absolute;left:0;top:0;width:720px;height:206px;background:var(--band)}
.wrap{position:absolute;left:85px;width:550px}

/* header */
.brand{position:absolute;left:85px;top:18px;display:flex;align-items:center;gap:8px}
.brand-mark{width:30px;height:30px;background:var(--lime)}
.brand-name{font-size:22px;font-weight:700;color:var(--navy);letter-spacing:.5px}
.social{display:flex;gap:2px}
.social span{width:19px;height:19px;display:block}
.social .fb{background:var(--fb)}.social .tw{background:var(--tw)}.social .li{background:var(--li)}
.header-social{position:absolute;left:433px;top:29px}
.search{position:absolute;left:502px;top:25px;width:133px;height:27px;background:#fff;border:1px solid #ddd;display:flex;align-items:center;justify-content:space-between;padding-left:14px;clip-path:polygon(6px 0,100% 0,100% 100%,6px 100%,0 50%)}
.search em{font-style:normal;font-size:7px;color:#aaa}
.search b{width:24px;height:21px;margin-right:3px;background:var(--fb);display:flex;align-items:center;justify-content:center}

/* nav */
.nav{top:67px;height:29px;background:var(--lime);display:flex;align-items:center;justify-content:space-between;padding:0 10px}
.nav a{font-size:8.6px;font-weight:600;color:#fff;text-transform:uppercase;text-decoration:none;padding:7px 8px}
.nav a.active{background:var(--navy);clip-path:polygon(6px 0,100% 0,calc(100% - 6px) 50%,100% 100%,6px 100%,0 50%,6px 0);padding:7px 14px}

/* hero */
.hero{top:96px;height:289px;overflow:hidden;background:linear-gradient(160deg,#6c8a3c 0%,#3c5a2a 35%,#7c7a5e 60%,#4d4a3c 100%)}
.hero-shadow{top:385px;height:14px;background:radial-gradient(ellipse at top,rgba(0,0,0,.18),transparent 70%)}
.hero h1{position:absolute;top:128px;width:100%;text-align:center;color:#fff;font-size:17px;font-weight:700;text-shadow:0 1px 3px rgba(0,0,0,.5)}
.thumbs{position:absolute;top:164px;left:135px;display:flex;gap:8px}
.thumbs i{width:64px;height:28px;border:3px solid #ddd;background:#5e6e3c}
.thumbs i.on{border-color:#fff;background:#6f8a40}
.arrow-btn{position:absolute;top:128px;width:28px;height:28px;border-radius:50%;background:rgba(255,255,255,.25)}
.arrow-btn.prev{left:11px}.arrow-btn.next{right:11px}
.cta{position:absolute;top:210px;left:197px;width:156px;height:24px;background:var(--orange);color:#fff;font-weight:600;font-size:12.5px;display:flex;align-items:center;justify-content:center;clip-path:polygon(0 0,100% 0,94% 50%,100% 100%,0 100%,6% 50%)}

/* intro */
.intro{top:406px;font-size:12px;line-height:15px;color:var(--navy)}
.intro svg{vertical-align:middle;margin-left:6px}
.section-title{text-align:center;font-size:14.5px;font-weight:700;color:var(--navy);letter-spacing:.3px}
.t-what{top:453px}.t-land{top:716px}

/* panels */
.panels{top:494px;height:186px;display:flex;gap:1px}
.panel{flex:1;position:relative;padding:16px 18px 0;color:#111}
.panel.styles{background:var(--lime)}
.panel.install{background:var(--navy);color:#fff}
.panel h2{text-align:center;font-size:14.5px;font-weight:700;margin-bottom:6px}
.panel p{font-size:9.4px;line-height:12px}
.hexes{position:absolute;top:76px;left:18px;display:flex}
.hex{width:80px;height:90px;background:#fff;color:#333;clip-path:polygon(50% 0,100% 25%,100% 75%,50% 100%,0 75%,0 25%);display:flex;align-items:center;justify-content:center;text-align:center;font-size:10px;line-height:12px}
.more{position:absolute;bottom:-9px;left:90px;width:95px;height:17px;background:var(--orange);color:#fff;font-size:9.5px;display:flex;align-items:center;justify-content:center;clip-path:polygon(0 0,100% 0,94% 50%,100% 100%,0 100%,6% 50%)}

/* landscapes */
.gallery{top:758px;display:flex;gap:5px}
.card{width:106px}
.card .photo{height:75px;border:1px solid #ddd;padding:4px;background:#fff}
.card .photo div{width:100%;height:100%}
.card h3{font-size:9.6px;font-weight:400;color:var(--navy);margin-top:9px}
.card p{font-size:6.8px;line-height:8px;margin-top:3px;color:#222}

/* map */
.map{top:906px;height:204px;background:linear-gradient(135deg,#e7ecd9 0%,#dfe6cf 50%,#cfdde6 100%)}
.address{position:absolute;left:25px;top:40px;width:176px;height:118px;background:rgba(40,40,40,.85);padding:14px 15px;color:#fff}
.address .tag{display:inline-block;background:var(--navy);font-size:6.8px;padding:1px 8px;text-transform:uppercase;margin-bottom:2px}
.address p{font-size:9px;line-height:11.5px;margin-bottom:6px}
.pin{position:absolute;left:353px;top:90px}

/* footer */
.footer{top:1138px;font-size:6.2px;line-height:7.5px;color:#222}
.footer-social{position:absolute;left:574px;top:1133px}
</style>
</head>
<body>
<div class="top-band"></div>

<header>
  <div class="brand"><span class="brand-mark"></span><span class="brand-name">Glimmerseal</span></div>
  <div class="social header-social" aria-label="Social links"><span class="fb"></span><span class="tw"></span><span class="li"></span></div>
  <div class="search"><em>SEARCH</em><b><svg width="9" height="9" viewBox="0 0 10 10"><circle cx="4" cy="4" r="3" fill="none" stroke="#fff" stroke-width="1.5"/><line x1="6.3" y1="6.3" x2="9" y2="9" stroke="#fff" stroke-width="1.5"/></svg></b></div>
</header>

<nav class="wrap nav">
  <a>Home</a><a>About Us</a><a class="active">Happenings</a><a>Gallery</a><a>Liner Styles</a><a>Preparation</a><a>Installation</a><a>Contact Us</a>
</nav>

<section class="wrap hero" role="img" aria-label="Garden pond with waterfall, ferns and a rustic ladder">
  <span class="arrow-btn prev"></span><span class="arrow-btn next"></span>
  <h1>GLIMMERSEAL LOREM IPSUM DUMMY SLOGAN</h1>
  <div class="thumbs"><i class="on"></i><i></i><i></i><i></i></div>
  <div class="cta">Get in Touch with</div>
</section>
<div class="wrap hero-shadow"></div>

<p class="wrap intro">Glimmerseal has been manufactured, marketed and installed throughout Australia and the Pacific Rim since the early 1980's for a variety of domestic and commercial applications.<svg width="14" height="10" viewBox="0 0 14 10"><path d="M1 5h11M8 1l4 4-4 4" fill="none" stroke="#f47a10" stroke-width="2"/></svg></p>

<h2 class="wrap section-title t-what">WHAT WE DO?</h2>

<section class="wrap panels">
  <div class="panel styles">
    <h2>Liner Styles</h2>
    <p>Glimmerseal pond liners can be made to suit any size or shape pond you can imagine, from a small feature...</p>
    <div class="hexes"><div class="hex">Flat Sheet<br>Liners</div><div class="hex">Composite<br>Liners</div><div class="hex">Profile<br>Liners</div></div>
    <div class="more">View all details</div>
  </div>
  <div class="panel install">
    <h2>Installation</h2>
    <p>Installing your Glimmerseal pond liner is an easy task, unfortunately there is no one single correct way...</p>
    <div class="hexes"><div class="hex">Standard<br>Installation</div><div class="hex">Folding<br>Corners</div><div class="hex">Pipes &amp;<br>Penetrations</div></div>
    <div class="more">View all details</div>
  </div>
</section>

<h2 class="wrap section-title t-land">OUR LANDSCAPES</h2>

<section class="wrap gallery">
  <div class="card"><div class="photo"><div role="img" aria-label="Shopfront framed with green plantings" style="background:linear-gradient(#6f7a5a,#3f4a34)"></div></div><h3>Landscape Photo 1</h3><p>Nulla non neque. Phasellus libero magna...</p></div>
  <div class="card"><div class="photo"><div role="img" aria-label="Garden bed with sculpture and grasses" style="background:linear-gradient(#8a9a6a,#5a6e3a)"></div></div><h3>Landscape Photo 1</h3><p>Nulla non neque. Phasellus libero magna...</p></div>
  <div class="card"><div class="photo"><div role="img" aria-label="Storefront with colourful flower display" style="background:linear-gradient(#5a3a2a,#a0603a)"></div></div><h3>Landscape Photo 1</h3><p>Nulla non neque. Phasellus libero magna...</p></div>
  <div class="card"><div class="photo"><div role="img" aria-label="Outdoor seating among planted garden" style="background:linear-gradient(#a0a08a,#6a6a4a)"></div></div><h3>Landscape Photo 1</h3><p>Nulla non neque. Phasellus libero magna...</p></div>
  <div class="card"><div class="photo"><div role="img" aria-label="Topiary garden sculpture on a street" style="background:linear-gradient(#8a7a6a,#4e6a3a)"></div></div><h3>Landscape Photo 1</h3><p>Nulla non neque. Phasellus libero magna...</p></div>
</section>

<section class="wrap map" role="img" aria-label="Road map of central Victoria showing the factory location">
  <div class="address">
    <span class="tag">Postal</span>
    <p>PO Box 2718, Larkwood North<br>Victoria, 3399, Australia</p>
    <span class="tag">Factory</span>
    <p>14-18 Fernbrook Way, Larkwood,<br>Victoria, 3399, Australia</p>
  </div>
  <svg class="pin" width="28" height="34" viewBox="0 0 28 34"><path d="M2 2h24v18L14 32 2 20z" fill="#fff" stroke="#0b3a78" stroke-width="2.5"/><circle cx="14" cy="13" r="4" fill="#0b3a78"/></svg>
</section>

<footer class="wrap footer">
  Home &nbsp;|&nbsp; About Us &nbsp;|&nbsp; Happenings &nbsp;|&nbsp; Gallery &nbsp;|&nbsp; Liner Styles &nbsp;|&nbsp; Preparation &nbsp;|&nbsp; Installation &nbsp;|&nbsp; Contact Us<br>
  Copyright © 2013 - Terms and Conditions
</footer>
<div class="social footer-social" aria-label="Social links"><span class="fb"></span><span class="tw"></span><span class="li"></span></div>
</body>
</html>
```